Long Established Local Fencing (not swords) Business needs fresh Business Cards

We need fresh double sided business cards for our Fencing Construction business, we are looking for something with our new logo design added, and maybe a photo background ?
We recently had cards made from Quillmarko and we were horrified with what we got back, the quality was terrible, so am looking for high quality format for good printing company to make.
We install Steelwave, Timber paling, Aluminium Slat Screening, Picket (timber and aluminium) and most other fencing installations.
Our website is brelbanfencing.com.au should you like to learn a bit more.
We do have logo in other formats if required.
We have been in business for over 35 years and we have used this as a "motto" it is on our signage

Industry/Entity Type

Construction

Contact Information for Business Card

Open to ideas, we need 3 x different cards, one generic with no name and 2 x others each with 1 of our bosses name on each, I will put into upload files.

Colors
ec1f27
000000
606060
f5f5f5

Requirements
Must have
• Company Name and Logo
• Address
• Contact details, phone, website, email etc
• Small space to write notes when leaving card at residence
Nice to have
• Our motto "Servicing the Peninsula for over 35 years"

```html
<!DOCTYPE html>
<html lang="en">
<head>
<meta charset="utf-8">
<title>Brelban Fencing – Business Cards</title>
<link rel="stylesheet" href="https://fonts.googleapis.com/css2?family=Open+Sans:ital,wght@0,400;0,700;0,800;1,400&display=swap">
<style>
  :root {
    --brand-red: #ec1f27;
    --brand-black: #000000;
    --card-black: #161616;
    --brand-grey: #606060;
    --paper: #f5f5f5;
    --stage: #d9d6d3;
    --text-light: #f2f2f2;
    --rule-dots: #8a8a8a;
  }
  * { box-sizing: border-box; margin: 0; padding: 0; }
  html, body {
    width: 1200px; height: 864px; overflow: hidden;
    background: var(--stage);
    font-family: "Open Sans", Arial, sans-serif;
  }
  .sheet { position: relative; width: 1200px; height: 864px; }

  .card {
    position: absolute; width: 540px; height: 330px;
    border-radius: 3px;
    box-shadow: 0 6px 18px rgba(0,0,0,.18);
    overflow: hidden;
  }

  /* Back: notes card */
  .card--notes { left: 40px; top: 150px; background: var(--paper); }
  .notes__brand {
    position: absolute; top: 34px; left: 0; right: 0;
    text-align: center;
    font-weight: 800; font-size: 17px; letter-spacing: 1px;
    color: var(--brand-black);
  }
  .notes__lines {
    position: absolute; left: 56px; right: 56px; top: 88px;
    list-style: none;
  }
  .notes__lines li {
    height: 34px;
    border-bottom: 1px dotted var(--rule-dots);
  }
  .notes__motto {
    position: absolute; left: 56px; bottom: 30px;
    font-style: italic; font-size: 13px; color: var(--brand-grey);
  }

  /* Front: contact card */
  .card--contact { left: 620px; top: 384px; background: var(--card-black); color: var(--text-light); }
  .contact__brand {
    position: absolute; right: 34px; top: 92px;
    display: flex; align-items: center; gap: 10px;
    font-weight: 800; font-size: 26px; line-height: 34px; letter-spacing: .5px;
    color: var(--text-light); white-space: nowrap;
  }
  .contact__brand .mark {
    width: 16px; height: 16px; border-radius: 50%; background: var(--brand-red);
  }
  .contact__name {
    position: absolute; left: 34px; top: 134px;
    font-weight: 700; font-size: 17px; line-height: 24px; color: var(--brand-red);
    text-transform: uppercase; letter-spacing: .3px;
  }
  .contact__rule {
    position: absolute; left: 34px; right: 34px; top: 166px;
    height: 1px; background: var(--text-light); opacity: .85;
  }
  .contact__list {
    position: absolute; left: 34px; top: 180px; list-style: none;
    font-size: 13.5px; line-height: 21px; white-space: nowrap;
  }
  .contact__list li { display: flex; align-items: center; gap: 8px; }
  .contact__list svg { width: 12px; height: 12px; fill: var(--text-light); flex: none; }
  .contact__legal {
    position: absolute; right: 34px; bottom: 26px;
    text-align: right; font-size: 14px; line-height: 20px; font-style: normal;
    white-space: nowrap;
  }
</style>
</head>
<body>
<main class="sheet">

  <section class="card card--notes" aria-label="Card back with notes space">
    <div class="notes__brand">BRELBAN FENCING</div>
    <ul class="notes__lines">
      <li></li><li></li><li></li><li></li><li></li>
    </ul>
    <p class="notes__motto">Servicing the Peninsula for over 35 years</p>
  </section>

  <section class="card card--contact" aria-label="Card front with contact details">
    <div class="contact__brand"><span class="mark" aria-hidden="true"></span>BRELBAN FENCING</div>
    <h1 class="contact__name">Darren Kelso</h1>
    <div class="contact__rule"></div>
    <ul class="contact__list">
      <li>
        <svg viewBox="0 0 24 24" aria-hidden="true"><path d="M6.6 10.8a15 15 0 0 0 6.6 6.6l2.2-2.2c.3-.3.7-.4 1-.2 1.1.4 2.3.6 3.6.6.6 0 1 .4 1 1V20c0 .6-.4 1-1 1A17 17 0 0 1 3 4c0-.6.4-1 1-1h3.5c.6 0 1 .4 1 1 0 1.3.2 2.5.6 3.6.1.3 0 .7-.2 1z"/></svg>
        (02)4355 0182
      </li>
      <li>
        <svg viewBox="0 0 24 24" aria-hidden="true"><path d="M7 1h10a2 2 0 0 1 2 2v18a2 2 0 0 1-2 2H7a2 2 0 0 1-2-2V3a2 2 0 0 1 2-2zm0 3v14h10V4zm5 15.5a1 1 0 1 0 0 2 1 1 0 0 0 0-2z"/></svg>
        0412 555 384
      </li>
      <li>
        <svg viewBox="0 0 24 24" aria-hidden="true"><path d="M2 5h20v14H2zm2 2v.5l8 5 8-5V7zm0 2.8V17h16V9.8l-8 5z"/></svg>
        brelbanfencing@mailnest.com
      </li>
      <li>
        <svg viewBox="0 0 24 24" aria-hidden="true"><path d="M12 2a10 10 0 1 0 0 20 10 10 0 0 0 0-20zm6.9 9h-3a15 15 0 0 0-1.3-5.6A8 8 0 0 1 18.9 11zM12 4c.9 1.2 1.8 3.6 1.9 7h-3.8c.1-3.4 1-5.8 1.9-7zM9.4 5.4A15 15 0 0 0 8.1 11h-3a8 8 0 0 1 4.3-5.6zM5.1 13h3a15 15 0 0 0 1.3 5.6A8 8 0 0 1 5.1 13zM12 20c-.9-1.2-1.8-3.6-1.9-7h3.8c-.1 3.4-1 5.8-1.9 7zm2.6-1.4a15 15 0 0 0 1.3-5.6h3a8 8 0 0 1-4.3 5.6z"/></svg>
        www.brelbanfencing.com.au
      </li>
    </ul>
    <address class="contact__legal">
      License No: 48120c<br>
      ABN 51 204 86 319<br>
      27 Corella Ave Brelban
    </address>
  </section>

</main>
</body>
</html>
```